MEDIATION & Organisationsentwicklung
Hervorragende Zusammenarbeit!Schnelle Bearbeitung der Änderungswünsche und sehr gutes Einfühlungsvermögen in die Denkweise und Anspruchshaltung des Kunden. Nur zu empfehlen und ich freue mich auf weitere Zusammenarbeit!
Zielgruppe
- Mediation: 1. Mediation bei Trennung & Scheidung, 2. Mediation im Erbfall, 3. Nachfolgeregelung in Familienunternehmen & betriebliche Konfliktklärung: Konfliktklärung im Unternehmenskontext
- Organisationsentwicklung: Teamentwicklung, Workshopmoderation, Großgruppenmoderation
Aufgabenstellung
Das Design sollte klar und präzise sein. Stichworte sind Vertrauen, Entwicklung, Verlässlichkeit

```html
<!DOCTYPE html>
<html lang="de">
<head>
<meta charset="utf-8">
<title>Dorothee Wulfen – Geschäftsausstattung</title>
<link rel="stylesheet" href="https://fonts.googleapis.com/css2?family=Open+Sans:wght@400;600&display=swap">
<style>
  :root {
    --brand-blue: #0b4a7a;
    --tagline-grey: #7d7d7d;
    --flap-grey: #c9d4d7;
    --paper: #ffffff;
    --ink-white: #ffffff;
    --stage: #ffffff;
  }
  html, body { margin: 0; padding: 0; overflow: hidden; }
  body {
    width: 1200px; height: 908px; position: relative;
    background: var(--stage);
    font-family: "Open Sans", Arial, sans-serif;
  }
  .piece { position: absolute; overflow: hidden; box-shadow: 2px 3px 8px rgba(0,0,0,0.18); }
  .piece svg.bg { position: absolute; inset: 0; }

  .wordmark { position: absolute; display: flex; align-items: center; gap: 8px; }
  .wordmark-name { font-weight: 600; line-height: 1.0; color: var(--brand-blue); margin: 0; white-space: nowrap; }
  .wordmark-dot { border-radius: 50%; background: var(--brand-blue); flex: none; }
  .wordmark-tagline { font-weight: 400; line-height: 1.1; color: var(--tagline-grey); margin: 0; white-space: nowrap; }
  .wordmark--white .wordmark-name,
  .wordmark--white .wordmark-tagline { color: var(--ink-white); }
  .wordmark--white .wordmark-dot { background: var(--ink-white); }

  .logo-sheet { left: 110px; top: 244px; }
  .logo-sheet .wordmark-name { font-size: 24px; }
  .logo-sheet .wordmark-dot { width: 44px; height: 44px; }
  .logo-sheet .wordmark-tagline { font-size: 14px; }

  .card-front { left: 97px; top: 389px; width: 313px; height: 202px; background: var(--brand-blue); }
  .card-front .wordmark { left: 29px; top: 56px; }
  .card-front .wordmark-name { font-size: 21px; }
  .card-front .wordmark-dot { width: 38px; height: 38px; }
  .card-front .wordmark-tagline { font-size: 13px; }

  .card-back { left: 97px; top: 608px; width: 313px; height: 203px; background: var(--paper); }
  .card-back .wordmark { left: 20px; top: 22px; gap: 6px; }
  .card-back .wordmark-name { font-size: 14px; }
  .card-back .wordmark-dot { width: 26px; height: 26px; }
  .card-back .wordmark-tagline { font-size: 9px; }
  .contact { position: absolute; top: 135px; color: var(--ink-white); font-size: 12px; line-height: 15px; margin: 0; }
  .contact--address { left: 25px; }
  .contact--web { left: 170px; }

  .letterhead { left: 435px; top: 177px; width: 427px; height: 638px; background: var(--paper); }
  .letterhead .wordmark { right: 26px; top: 22px; gap: 5px; }
  .letterhead .wordmark-name { font-size: 12px; }
  .letterhead .wordmark-dot { width: 22px; height: 22px; }
  .letterhead .wordmark-tagline { font-size: 7.5px; }
  .footer-col { position: absolute; top: 596px; color: var(--ink-white); font-size: 5px; line-height: 7px; font-weight: 600; margin: 0; }
  .footer-col--contact { left: 270px; }
  .footer-col--bank { left: 350px; }

  .envelope { left: 694px; top: 350px; width: 415px; height: 265px; box-shadow: none; }
  .envelope .wordmark { right: 20px; top: 76px; gap: 5px; }
  .envelope .wordmark-name { font-size: 12px; }
  .envelope .wordmark-dot { width: 22px; height: 22px; }
  .envelope .wordmark-tagline { font-size: 7.5px; }
  .envelope-address {
    position: absolute; right: 22px; top: 210px; margin: 0;
    text-align: right; color: var(--ink-white); font-size: 10.5px; line-height: 12.5px;
  }
</style>
</head>
<body>

  <div class="wordmark logo-sheet">
    <p class="wordmark-name">Dorothee<br>Wulfen</p>
    <span class="wordmark-dot"></span>
    <p class="wordmark-tagline">Mediation &amp;<br>Organisations-<br>entwicklung</p>
  </div>

  <section class="piece card-front" aria-label="Visitenkarte Vorderseite">
    <div class="wordmark wordmark--white">
      <p class="wordmark-name">Dorothee<br>Wulfen</p>
      <span class="wordmark-dot"></span>
      <p class="wordmark-tagline">Mediation &amp;<br>Organisations-<br>entwicklung</p>
    </div>
  </section>

  <section class="piece card-back" aria-label="Visitenkarte Rückseite">
    <svg class="bg" width="313" height="203" viewBox="0 0 313 203">
      <path d="M0,122 C130,112 250,70 313,0 L313,203 L0,203 Z" fill="var(--brand-blue)"/>
    </svg>
    <div class="wordmark">
      <p class="wordmark-name">Dorothee<br>Wulfen</p>
      <span class="wordmark-dot"></span>
      <p class="wordmark-tagline">Mediation &amp;<br>Organisations-<br>entwicklung</p>
    </div>
    <p class="contact contact--address">Lindenweg 7<br>48151 Feldhausen<br>Tel.: 0251 987 430</p>
    <p class="contact contact--web">Fax: 0251 987 439<br>info@dw-mediation.de<br>www.dw-mediation.de</p>
  </section>

  <section class="piece letterhead" aria-label="Briefbogen">
    <svg class="bg" width="427" height="638" viewBox="0 0 427 638">
      <path d="M0,606 C160,604 330,580 427,540 L427,638 L0,638 Z" fill="var(--brand-blue)"/>
    </svg>
    <div class="wordmark">
      <p class="wordmark-name">Dorothee<br>Wulfen</p>
      <span class="wordmark-dot"></span>
      <p class="wordmark-tagline">Mediation &amp;<br>Organisations-<br>entwicklung</p>
    </div>
    <p class="footer-col footer-col--contact">Tel. 0251 987 430<br>Fax 0251 987 439<br>info@dorothee-wulfen.de<br>www.dorothee-wulfen.de</p>
    <p class="footer-col footer-col--bank">Bank Feldhausen<br>IBAN DE 4400 71 230<br>BIC 582 604 117<br>Steuer-Nr. 0251 339 072</p>
  </section>

  <section class="piece envelope" aria-label="Briefumschlag">
    <svg class="bg" width="415" height="265" viewBox="0 0 415 265">
      <path d="M0,62 C10,40 120,8 210,0 L330,0 C370,4 405,34 415,62 Z" fill="var(--flap-grey)"/>
      <g transform="translate(0,60)" style="filter:drop-shadow(2px 3px 4px rgba(0,0,0,0.18))">
        <rect width="415" height="205" fill="var(--paper)"/>
        <path d="M0,172 C150,162 320,140 415,110 L415,205 L0,205 Z" fill="var(--brand-blue)"/>
        <rect x="40" y="95" width="157" height="80" rx="8" fill="var(--flap-grey)"/>
      </g>
    </svg>
    <div class="wordmark">
      <p class="wordmark-name">Dorothee<br>Wulfen</p>
      <span class="wordmark-dot"></span>
      <p class="wordmark-tagline">Mediation &amp;<br>Organisations-<br>entwicklung</p>
    </div>
    <p class="envelope-address">Lindenweg 7<br>48151 Feldhausen<br>Tel.: 0251 987 430</p>
  </section>

</body>
</html>
```